4th Generation Family Business Needs a New Card Design!

We are a family owned 4th Generation company. We are based in the Sydney, Australia area and we are desperately in need of a more modern and classy card. We are monumental masons who design, supply & erect lasting memorials throughout cemeteries in Sydney. Our customers are normally in a period of grieving. I have attached logo files that will need to be implemented on the card. Company was established 1935. Australian Owned and Operated. Card needs to be designed to PRINTLY.com specification.

Target Market(s)

Our target market is based upon people that a grieving for family members that have passed away. We also deal with alot of companies that own and operate cemeteries.

Industry/Entity Type

Business

Contact Information for Business Card

Oliver Brantley, Operations Manager, 0417552908, oliver@hollowaystoneworks.com.au
Martin Brantley, Director, 0431906627, martin@hollowaystoneworks.com.au
Phone # 02 9634 2258
Website: www.hollowaystoneworks.com.au
Address: Suite 17, 8 Calloway Lane, East Penrose, Sydney NSW 2290

Font styles to use
Serif
Decorative
Script

Requirements
Must have
• Would like to see the logo nicely implemented with a modern design. Embossed lettering would be a nice additive.

```html
<!DOCTYPE html>
<html lang="en">
<head>
<meta charset="utf-8">
<title>Holloway Stoneworks – Business Card</title>
<link rel="stylesheet" href="https://fonts.googleapis.com/css2?family=Open+Sans:wght@400;600&display=swap">
<style>
  :root {
    --page-bg: #e9e7e3;
    --card-bg: #ffffff;
    --ink-dark: #3b3b3b;
    --ink-mid: #5a5a5a;
    --rule: #8a8a8a;
    --accent-gold: #f2b824;
    --band-grey: #6e6e6e;
    --band-text: #ffffff;
  }
  * { margin: 0; padding: 0; box-sizing: border-box; }
  html, body {
    width: 1200px; height: 832px; overflow: hidden;
    background: var(--page-bg);
    font-family: "Open Sans", sans-serif;
  }
  .business-card {
    position: absolute; left: 100px; top: 133px;
    width: 1000px; height: 566px;
    background: var(--card-bg);
    box-shadow: 0 6px 22px rgba(0,0,0,0.18);
    overflow: hidden;
  }
  .brand {
    position: absolute; left: 62px; top: 80px;
    display: flex; align-items: center; gap: 14px;
  }
  .brand-square {
    width: 22px; height: 22px; background: var(--accent-gold);
  }
  .brand-name {
    font-weight: 600; font-size: 30px; line-height: 1.15;
    letter-spacing: 2px; color: var(--ink-dark); text-transform: uppercase;
  }
  .person {
    position: absolute; right: 58px; top: 222px; text-align: right;
  }
  .person-name {
    font-weight: 600; font-size: 29px; letter-spacing: 1.5px; color: var(--ink-dark);
    line-height: 1;
  }
  .person-title {
    margin-top: 12px; font-size: 20px; letter-spacing: 7px; color: var(--ink-dark);
    line-height: 1; margin-right: -7px;
  }
  .divider {
    position: absolute; left: 48px; right: 58px; top: 300px;
    height: 2px; background: var(--rule);
  }
  .person-mobile {
    position: absolute; right: 58px; top: 312px;
    font-size: 20px; letter-spacing: 3px; color: var(--ink-dark); line-height: 1;
  }
  .contact-list {
    position: absolute; left: 58px; top: 362px; list-style: none;
  }
  .contact-item {
    display: flex; align-items: center; height: 36px;
    font-size: 26px; color: var(--ink-mid);
  }
  .contact-icon { width: 22px; height: 22px; margin-right: 20px; flex: none; }
  .address-band {
    position: absolute; left: 0; right: 0; bottom: 0; height: 72px;
    background: var(--band-grey);
    display: flex; align-items: center; padding-left: 58px;
    color: var(--band-text); font-size: 26px;
  }
  .address-band .contact-icon { width: 22px; height: 28px; }
</style>
</head>
<body>
  <div class="business-card">
    <div class="brand">
      <span class="brand-square"></span>
      <span class="brand-name">Holloway<br>Stoneworks</span>
    </div>

    <div class="person">
      <div class="person-name">MARTIN BRANTLEY</div>
      <div class="person-title">DIRECTOR</div>
    </div>
    <div class="divider"></div>
    <div class="person-mobile">0431906627</div>

    <ul class="contact-list">
      <li class="contact-item">
        <svg class="contact-icon" viewBox="0 0 24 24" aria-hidden="true">
          <rect x="1" y="5" width="22" height="15" fill="var(--accent-gold)"/>
          <path d="M1 5 L12 13 L23 5" fill="none" stroke="#fff" stroke-width="1.8"/>
        </svg>
        martin@hollowaystoneworks.com.au
      </li>
      <li class="contact-item">
        <svg class="contact-icon" viewBox="0 0 24 24" aria-hidden="true">
          <path d="M6.6 10.8a15.2 15.2 0 0 0 6.6 6.6l2.2-2.2a1 1 0 0 1 1-.25 11.4 11.4 0 0 0 3.6.6 1 1 0 0 1 1 1V20a1 1 0 0 1-1 1A17 17 0 0 1 3 4a1 1 0 0 1 1-1h3.5a1 1 0 0 1 1 1c0 1.25.2 2.45.57 3.57a1 1 0 0 1-.25 1L6.6 10.8z" fill="var(--accent-gold)"/>
        </svg>
        02 9634 2258
      </li>
      <li class="contact-item">
        <svg class="contact-icon" viewBox="0 0 24 24" aria-hidden="true">
          <g fill="none" stroke="var(--accent-gold)" stroke-width="2">
            <circle cx="12" cy="12" r="10"/>
            <ellipse cx="12" cy="12" rx="4.5" ry="10"/>
            <path d="M2 12h20M4 7h16M4 17h16"/>
          </g>
        </svg>
        hollowaystoneworks.com.au
      </li>
    </ul>

    <div class="address-band">
      <svg class="contact-icon" viewBox="0 0 20 28" aria-hidden="true">
        <path d="M10 1a9 9 0 0 0-9 9c0 7 9 17 9 17s9-10 9-17a9 9 0 0 0-9-9z" fill="var(--accent-gold)"/>
        <circle cx="10" cy="10" r="3.5" fill="var(--band-grey)"/>
      </svg>
      Suite 17, 8 Calloway Lane, East Penrose, Sydney NSW 2290
    </div>
  </div>
</body>
</html>
```